Photo Scanning New Business, Needs flyer design to capture Christmas gift ideas

Need a A5 size flyer for our business. Were a new business offering photo scanning and just about to go online. customers send us their old photos, slides or negatives from under their beds or in their cupboards and we then scan and digitize them and place onto a dvd or usb stick so they can view on their tv or computer anytime anywhere. Scanning old pictures isnt new bt very time consuming. Many customers like to download their photos from their digital cameras onto different social media websites, but their old photos they cant. Old photos also degrade and can get damaged.

I have included a design i was messing around with, which gives you the concept and wording im trying to get across in this flyer.

Target Market(s)

35 years and older. family members

Industry/Entity Type

Computer

Requirements
Must have
• the add must show the offer of "500 photos scanned for $50.00 Only"
Also have some words around " Make a great Christmas gift"

Needs to describe what the business is about
Nice to have
• please see my a5 flyer deisgn. colourful pictures. the flyer will be aimed at the christmas market, and hoping that people look at this and think that $50 is not alot of money for a christmas gift for one of the family, and that having all their pictures scanned is actually a good idea. Keeps them safe from Fire, Flood and Damage.
Should not have
• should not use cartoon style design

```html
<!DOCTYPE html>
<html lang="en">
<head>
<meta charset="utf-8">
<title>FrameSafe Christmas Flyer</title>
<link rel="stylesheet" href="https://fonts.googleapis.com/css2?family=Jost:ital,wght@0,400;0,500;1,400&display=swap">
<style>
  :root {
    --panel-blue: #5b9aba;
    --gap-white: #ffffff;
    --ink-white: #ffffff;
    --tree-white: #f6fafc;
    --tree-mid: #cfe2ec;
  }
  * { margin: 0; padding: 0; box-sizing: border-box; }
  html, body {
    width: 1200px; height: 812px; overflow: hidden;
    background: var(--gap-white);
    font-family: "Jost", "Futura", sans-serif;
    color: var(--ink-white);
  }
  .canvas { position: relative; width: 1200px; height: 812px; }
  .panel { position: absolute; top: 0; height: 812px; background: var(--panel-blue); }
  .panel--cover { left: 0; width: 572px; }
  .panel--info { left: 627px; width: 573px; }

  .tree-artwork {
    position: absolute; left: 86px; top: 188px; width: 402px; height: 437px;
    background:
      radial-gradient(closest-side at 50% 52%,
        var(--tree-white) 0%,
        var(--tree-white) 38%,
        var(--tree-mid) 70%,
        rgba(91,154,186,0) 100%);
  }
  .brand {
    position: absolute; left: 0; width: 572px; top: 756px;
    display: flex; justify-content: center; align-items: center; gap: 8px;
    font-size: 22px; font-weight: 500; letter-spacing: -0.3px;
  }
  .brand__mark { width: 14px; height: 14px; background: var(--ink-white); }

  .info-frame {
    position: absolute; left: 20px; top: 17px; width: 533px; height: 778px;
    border: 1.5px solid var(--ink-white);
  }
  .headline {
    position: absolute; left: 78px; width: 417px; top: 34px;
    text-align: center; font-size: 22px; font-weight: 400; letter-spacing: 0.3px;
    line-height: 26px;
    border-bottom: 1.5px solid var(--ink-white); padding-bottom: 1px;
  }
  .subhead {
    position: absolute; left: 0; width: 573px; top: 67px;
    text-align: center; font-size: 13px; letter-spacing: 0.4px;
  }
  .workflow { position: absolute; left: 0; top: 0; }
  .workflow text { font-family: "Jost", sans-serif; font-size: 9px; fill: var(--ink-white); }

  .benefits {
    position: absolute; left: 78px; width: 417px; top: 537px;
    border-top: 1.5px solid var(--ink-white); border-bottom: 1.5px solid var(--ink-white);
    padding: 3px 0 4px; list-style: none; text-align: center;
    font-size: 14px; line-height: 19.7px;
  }
  .web-address { position: absolute; left: 79px; top: 643px; font-size: 8.5px; line-height: 10px; }
  .offer {
    position: absolute; left: 0; width: 573px; top: 692px;
    text-align: center; font-style: italic; font-size: 21px; line-height: 26px;
    letter-spacing: 1px; text-transform: uppercase;
  }
</style>
</head>
<body>
<div class="canvas">
  <section class="panel panel--cover">
    <div class="tree-artwork" role="img" aria-label="Christmas tree illustration in white with a star on top and bead garlands"></div>
    <div class="brand"><span class="brand__mark"></span><span class="brand__name">FrameSafe</span></div>
  </section>

  <section class="panel panel--info">
    <div class="info-frame"></div>
    <h1 class="headline">BRING BACK TO LIFE YOUR OLD PHOTOS</h1>
    <p class="subhead">Photo, Slide and Negative Scanning</p>

    <svg class="workflow" width="573" height="812" viewBox="627 0 573 812" aria-label="Scanning workflow">
      <g fill="#fff" stroke="none">
        <rect x="717" y="336" width="38" height="26" rx="3"/>
        <rect x="728" y="331" width="12" height="6" rx="1"/>
        <circle cx="737" cy="349" r="8" fill="var(--panel-blue)"/>
        <circle cx="737" cy="349" r="5"/>
        <rect x="838" y="333" width="22" height="7"/>
        <rect x="832" y="342" width="36" height="12" rx="2"/>
        <rect x="838" y="355" width="22" height="7"/>
        <g transform="translate(970 345)">
          <rect x="-3.5" y="-16" width="7" height="32"/>
          <rect x="-3.5" y="-16" width="7" height="32" transform="rotate(45)"/>
          <rect x="-3.5" y="-16" width="7" height="32" transform="rotate(90)"/>
          <rect x="-3.5" y="-16" width="7" height="32" transform="rotate(135)"/>
          <circle r="11"/>
          <circle r="5" fill="var(--panel-blue)"/>
        </g>
        <circle cx="970" cy="171" r="15"/>
        <circle cx="970" cy="211" r="15"/>
        <circle cx="970" cy="251" r="15"/>
        <circle cx="1060" cy="256" r="6"/>
        <path d="M1049 281 q0-16 11-16 q11 0 11 16z"/>
        <circle cx="1074" cy="259" r="5.5"/>
        <path d="M1067 281 q1-14 8-14 q10 0 10 14z"/>
        <rect x="1065" y="331" width="36" height="8" rx="2"/>
        <rect x="1067" y="341" width="32" height="21" rx="2"/>
        <rect x="1077" y="345" width="12" height="4" rx="1" fill="var(--panel-blue)"/>
        <path d="M1116 350 h8 v5 h18 v-5 h8 v12 h-34z"/>
        <path d="M1133 330 l9 10 h-6 v10 h-6 v-10 h-6z"/>
        <rect x="1052" y="404" width="34" height="22" rx="1"/>
        <path d="M1052 405 l17 12 l17 -12" fill="none" stroke="var(--panel-blue)" stroke-width="2"/>
        <rect x="954" y="430" width="34" height="24" rx="2"/>
        <rect x="958" y="434" width="26" height="16" fill="var(--panel-blue)"/>
        <rect x="966" y="454" width="10" height="4"/>
        <rect x="998" y="430" width="20" height="32" rx="3"/>
        <rect x="1001" y="435" width="14" height="21" fill="var(--panel-blue)"/>
      </g>
      <g stroke="#fff" stroke-width="1.5" fill="#fff">
        <line x1="775" y1="347" x2="818" y2="347"/>
        <path d="M816 343 l7 4 l-7 4z" stroke="none"/>
        <line x1="887" y1="347" x2="930" y2="347"/>
        <path d="M928 343 l7 4 l-7 4z" stroke="none"/>
      </g>
      <g stroke="#fff" stroke-width="1.3" stroke-dasharray="5 4" fill="none">
        <line x1="970" y1="270" x2="970" y2="322"/>
        <line x1="970" y1="380" x2="970" y2="425"/>
        <line x1="1012" y1="346" x2="1057" y2="346"/>
        <line x1="1012" y1="319" x2="1045" y2="287"/>
        <line x1="1012" y1="368" x2="1045" y2="400"/>
      </g>
      <g text-anchor="middle">
        <text x="970" y="146">Socialize it</text>
        <text x="1065" y="243">Share it</text>
        <text x="737" y="373">Take your old photo</text>
        <text x="850" y="373">Scan it</text>
        <text x="972" y="373">Process it</text>
        <text x="1091" y="373">Archive it</text>
        <text x="1069" y="437">Send it</text>
        <text x="972" y="475">Show it</text>
      </g>
    </svg>

    <ul class="benefits">
      <li>Don't keep your Treasured old photos under the bed anymore</li>
      <li>Breath new life into them</li>
      <li>Preserve them for life</li>
      <li>Digitize them and watch on your TV or Computer anytime</li>
      <li>Protect them from Fire, Flood or Damage</li>
    </ul>
    <p class="web-address">www.framesafe.com.au</p>
    <p class="offer">Make a great Christmas gift<br>500 photos scanned for only $50.00</p>
  </section>
</div>
</body>
</html>
```